Spy/Espionage/Counterintelligence Membership Community Needs a PowerPoint Template

We need a powerpoint template for one of our business verticals focused on spies, espionage, and counterintelligence. The name of it is "Pale Harbor Guild" and the logo is attached. Pale Harbor Guild is a community that connects people with experts in espionage and counterintelligence through an online social network, as well as in-person events. We would like to see designs that incorporate the red and black of the logo. The design should communicate mystery/suspense and peak curiosity.

Target Market(s)

Late 20s to baby boomers, male

Industry/Entity Type

Social Club

Font styles to use
Sans Serif

Colors
ec1f27
000000
ffffff

Requirements
Must have
• A user-friendly ppt template file. Incorporate basic fonts that don't have to be installed on every computer for presentations. A cover slide and a basic inside slide. A white background. I will also need graphic source files.
Nice to have
• Plenty of space for slide title and body content. Logo on every slide.
Should not have
• Inconsistency with fonts. Misalignment of images.

```html
<!DOCTYPE html>
<html lang="en">
<head>
<meta charset="utf-8">
<title>Pale Harbor Guild – Presentation Template</title>
<link href="https://fonts.googleapis.com/css2?family=Montserrat:wght@400;600;700;800&family=Nunito+Sans:wght@400;700&display=swap" rel="stylesheet">
<style>
:root{
  --red:#ec1f27;
  --red-dark:#c5141b;
  --black:#000;
  --ink:#333;
  --charcoal:#404040;
  --white:#fff;
  --paper-top:#fbfbfb;
  --paper-bottom:#dedede;
  --grey-row:#cfcfcf;
  --grey-head:#b5b5b5;
}
*{box-sizing:border-box;margin:0;padding:0}
html,body{width:1061px;height:1200px;overflow:hidden;background:var(--black)}
body{position:relative;font-family:"Nunito Sans",Arial,sans-serif;color:var(--ink)}
.slide{position:absolute;width:519px;height:389px;overflow:hidden;
  background:linear-gradient(180deg,var(--paper-top) 0%,#f1f1f1 55%,var(--paper-bottom) 100%)}
.col-a{left:9px}.col-b{left:536px}
.row-1{top:9px}.row-2{top:407px}.row-3{top:805px}

/* cover & closing */
.top-tab{position:absolute;top:0;left:104px;width:312px;height:10px;background:var(--red);
  clip-path:polygon(0 0,100% 0,97% 100%,3% 100%)}
.red-band{position:absolute;left:0;right:0;top:130px;height:121px;background:var(--red)}
.badge{position:absolute;left:106px;top:129px;width:302px;height:96px;border-radius:7px;
  background:linear-gradient(180deg,#4a4a4a 0%,#1b1b1b 60%,#111 100%);
  box-shadow:0 3px 6px rgba(0,0,0,.45);text-align:center}
.badge .title{font-family:Montserrat,Arial,sans-serif;font-weight:700;font-size:38px;color:#f0f0f0;
  letter-spacing:-.5px;margin-top:12px;line-height:44px}
.badge .subtitle{font-family:Montserrat,Arial,sans-serif;font-size:21px;color:var(--red);line-height:24px}
.badge .thanks{font-family:Montserrat,Arial,sans-serif;font-weight:700;font-size:42px;color:#f0f0f0;line-height:96px}
.chevron{position:absolute;top:140px;width:32px;height:69px}
.chevron.left{left:60px}.chevron.right{left:424px}
.bottom-bar{position:absolute;left:0;right:0;bottom:0;height:16px;background:var(--red)}
.brand-lockup{position:absolute;left:22px;top:270px;width:160px;text-align:center}
.brand-mark{display:block;width:56px;height:56px;border-radius:50%;background:var(--red);
  border:2px solid var(--black);margin:0 auto 4px}
.brand-name{font-family:"Nunito Sans",Arial,sans-serif;font-size:19px;color:var(--black);white-space:nowrap}
.presenter{position:absolute;right:20px;top:294px;text-align:right;font-family:Montserrat,Arial,sans-serif}
.presenter .by{font-size:15px;color:var(--charcoal)}
.presenter .name{font-size:16px;font-weight:700;color:var(--red);margin-top:2px}

/* inner slides */
.ribbon{position:absolute;top:26px;width:12px;height:22px;background:var(--red)}
.ribbon.left{left:0;clip-path:polygon(0 0,100% 0,70% 50%,100% 100%,0 100%)}
.ribbon.right{right:0;clip-path:polygon(0 0,100% 0,100% 100%,0 100%,30% 50%)}
.slide-title{position:absolute;left:21px;top:16px;font-family:Montserrat,Arial,sans-serif;
  font-weight:700;font-size:29px;color:var(--charcoal);letter-spacing:-.3px}
.slide-title em{font-style:normal;color:var(--red)}
.footer{position:absolute;left:0;right:0;top:353px;height:36px;border-top:1px solid var(--red)}
.footer .brand-name{position:absolute;left:21px;top:7px;font-size:17px}
.pager{position:absolute;right:40px;top:8px;display:flex;gap:4px}
.pager span{width:22px;height:20px;border-radius:3px;background:linear-gradient(#4a4a4a,#1e1e1e);
  display:flex;align-items:center;justify-content:center}
.page-no{position:absolute;right:12px;top:8px;height:20px;padding-left:9px;border-left:1px solid #999;
  font-size:13px;line-height:20px;color:#555}

.about{position:absolute;left:21px;top:70px;width:477px;font-size:13.6px;line-height:18px;color:#3a3a3a;text-align:justify}
.about p{margin-bottom:11px}
.about b{color:var(--charcoal)}

.services{position:absolute;left:42px;top:72px;list-style:none;font-family:Montserrat,Arial,sans-serif;
  font-size:17.5px;color:var(--charcoal)}
.services li{height:25px;line-height:25px;padding-left:20px;position:relative}
.services li::before{content:"";position:absolute;left:2px;top:9px;width:7px;height:7px;background:var(--red);transform:rotate(45deg)}
.team-photo{position:absolute;left:232px;top:78px;width:258px;height:232px;border-radius:4px;
  background:radial-gradient(ellipse at 50% 55%,#4b4b4b 0%,#2a2a2a 45%,rgba(240,240,240,0) 72%)}

.grid-table{position:absolute;left:24px;top:73px;width:469px;border-collapse:collapse;font-size:9.5px;table-layout:fixed}
.grid-table th{height:25px;font-family:Montserrat,Arial,sans-serif;font-size:13px;font-weight:700}
.grid-table th.cat{background:var(--grey-head);color:#333;width:233px}
.grid-table th.o1{background:var(--red);color:var(--white);width:117px}
.grid-table th.o2{background:#4a4a4a;color:var(--white)}
.grid-table td{height:18.1px;padding:0}
.grid-table tr.group td{background:var(--grey-row);font-weight:700;padding-left:6px;color:#333}
.grid-table td.label{padding-left:30px;color:#555;background:var(--white)}
.grid-table tr.alt td.label{background:#f0f0f0}
.grid-table td.yes{background:var(--red);color:var(--white);text-align:center}
.grid-table tr.alt td.yes{background:#e0353b}
.grid-table td.dash{background:#4a4a4a;color:#ddd;text-align:center}
.grid-table tr.alt td.dash{background:#6b6b6b}

.map-frame{position:absolute;left:31px;top:72px;width:222px;height:222px;background:#fff;padding:4px;
  box-shadow:0 1px 3px rgba(0,0,0,.3)}
.map-fill{width:100%;height:100%;background:linear-gradient(160deg,#e4e7c8 0%,#d9dfb5 45%,#a9c6e0 70%,#8fb6db 100%)}
.contact{position:absolute;left:266px;top:72px;width:236px;font-size:9.4px;line-height:11.5px;color:#444}
.contact p.intro{text-align:justify;margin-bottom:7px}
.contact p.intro b{color:var(--red)}
.contact h4{color:var(--red);font-size:11px;font-weight:700;margin-top:4px;line-height:14px}
.socials{position:absolute;left:34px;top:315px;display:flex;align-items:center;gap:9px;
  font-family:Montserrat,Arial,sans-serif;font-size:12px;color:#444}
.socials i{display:block;width:18px;height:18px;background:var(--red);border-radius:2px}
.socials b{color:var(--red);font-weight:600}
.socials span{margin-left:-2px}
.closing .brand-lockup{top:262px;width:170px}
.closing .brand-mark{width:60px;height:60px}
.closing .brand-name{font-size:21px}
.closing .presenter{top:280px}
</style>
</head>
<body>

<section class="slide cover col-a row-1">
  <div class="top-tab"></div>
  <div class="red-band"></div>
  <svg class="chevron left" viewBox="0 0 32 69"><polygon points="32,0 32,69 0,34.5" fill="#fff"/><polygon points="32,14 32,55 13,34.5" fill="#ec1f27"/></svg>
  <div class="badge"><div class="title">Title Project</div><div class="subtitle">subtext presentation</div></div>
  <svg class="chevron right" viewBox="0 0 32 69"><polygon points="0,0 0,69 32,34.5" fill="#fff"/><polygon points="0,14 0,55 19,34.5" fill="#ec1f27"/></svg>
  <div class="brand-lockup"><span class="brand-mark"></span><div class="brand-name">Pale Harbor Guild</div></div>
  <div class="presenter"><div class="by">Presentation by</div><div class="name">Daniel Hart</div></div>
  <div class="bottom-bar"></div>
</section>

<section class="slide about-slide col-b row-1">
  <span class="ribbon left"></span><span class="ribbon right"></span>
  <h2 class="slide-title">About Company</h2>
  <div class="about">
    <p><b>Lorem ipsum</b> dolor sit amet, consectetuer adipiscing elit. Maecenas porttitor congue massa. Fusce posuere, magna sed pulvinar ultricies, purus lectus malesuada libero, sit amet commodo magna eros quis urna.</p>
    <p><b>Nunc viverra imperdiet enim</b>. Fusce est. Vivamus a tellus. Pellentesque habitant morbi tristique senectus et netus et malesuada fames ac turpis egestas. Proin pharetra nonummy pede. Mauris et orci.</p>
    <p><b>Aenean nec lorem.</b> In porttitor. Donec laoreet nonummy augue.</p>
    <p>Suspendisse dui purus, scelerisque at, vulputate vitae, pretium mattis, nunc. Mauris eget neque at sem venenatis eleifend. Ut nonummy.</p>
    <p><b>Fusce aliquet pede non pede.</b><br>Suspendisse dapibus lorem pellentesque magna. Integer nulla.</p>
  </div>
  <footer class="footer"><span class="brand-name">Pale Harbor Guild</span>
    <div class="pager"><span><svg width="10" height="12" viewBox="0 0 10 12"><polyline points="7,1 2,6 7,11" fill="none" stroke="#fff" stroke-width="2.4"/></svg></span><span><svg width="10" height="12" viewBox="0 0 10 12"><polyline points="3,1 8,6 3,11" fill="none" stroke="#fff" stroke-width="2.4"/></svg></span></div>
    <span class="page-no">2</span></footer>
</section>

<section class="slide services-slide col-a row-2">
  <span class="ribbon left"></span><span class="ribbon right"></span>
  <h2 class="slide-title"><em>Our</em> Services</h2>
  <ul class="services">
    <li>Lorem ipsum</li><li>Lorem ipsum</li><li>Lorem ipsum</li><li>Lorem ipsum</li><li>Lorem ipsum</li>
    <li>Lorem ipsum</li><li>Lorem ipsum</li><li>Lorem ipsum</li><li>Lorem ipsum</li><li>Lorem ipsum</li>
  </ul>
  <div class="team-photo" role="img" aria-label="Photo of a team of business people in dark suits standing together"></div>
  <footer class="footer"><span class="brand-name">Pale Harbor Guild</span>
    <div class="pager"><span><svg width="10" height="12" viewBox="0 0 10 12"><polyline points="7,1 2,6 7,11" fill="none" stroke="#fff" stroke-width="2.4"/></svg></span><span><svg width="10" height="12" viewBox="0 0 10 12"><polyline points="3,1 8,6 3,11" fill="none" stroke="#fff" stroke-width="2.4"/></svg></span></div>
    <span class="page-no">3</span></footer>
</section>

<section class="slide table-slide col-b row-2">
  <span class="ribbon left"></span><span class="ribbon right"></span>
  <h2 class="slide-title"><em>Table</em> Presentation</h2>
  <table class="grid-table">
    <tr><th class="cat">CATEGORY</th><th class="o1">OPTION 1</th><th class="o2">OPTION 2</th></tr>
    <tr class="group"><td colspan="3">Category 1</td></tr>
    <tr><td class="label">Lorem ipsum dolor sit amet</td><td class="yes">Yes</td><td class="dash">-</td></tr>
    <tr class="alt"><td class="label">Lorem ipsum dolor sit amet</td><td class="yes">Yes</td><td class="dash">-</td></tr>
    <tr><td class="label">Lorem ipsum dolor sit amet</td><td class="yes">Yes</td><td class="dash">-</td></tr>
    <tr class="group"><td colspan="3">Category 2</td></tr>
    <tr><td class="label">Lorem ipsum dolor sit amet</td><td class="yes">Yes</td><td class="dash">-</td></tr>
    <tr class="alt"><td class="label">Lorem ipsum dolor sit amet</td><td class="yes">Yes</td><td class="dash">-</td></tr>
    <tr><td class="label">Lorem ipsum dolor sit amet</td><td class="yes">Yes</td><td class="dash">-</td></tr>
    <tr class="alt"><td class="label">Lorem ipsum dolor sit amet</td><td class="yes">Yes</td><td class="dash">-</td></tr>
    <tr class="group"><td colspan="3">Category 3</td></tr>
    <tr><td class="label">Lorem ipsum dolor sit amet</td><td class="yes">Yes</td><td class="dash">-</td></tr>
    <tr class="alt"><td class="label">Lorem ipsum dolor sit amet</td><td class="yes">Yes</td><td class="dash">-</td></tr>
  </table>
  <footer class="footer"><span class="brand-name">Pale Harbor Guild</span>
    <div class="pager"><span><svg width="10" height="12" viewBox="0 0 10 12"><polyline points="7,1 2,6 7,11" fill="none" stroke="#fff" stroke-width="2.4"/></svg></span><span><svg width="10" height="12" viewBox="0 0 10 12"><polyline points="3,1 8,6 3,11" fill="none" stroke="#fff" stroke-width="2.4"/></svg></span></div>
    <span class="page-no">4</span></footer>
</section>

<section class="slide contact-slide col-a row-3">
  <span class="ribbon left"></span><span class="ribbon right"></span>
  <h2 class="slide-title"><em>Contact</em> Info</h2>
  <div class="map-frame"><div class="map-fill" role="img" aria-label="Map of Europe and the Mediterranean region"></div></div>
  <div class="contact">
    <p class="intro"><b>Lorem ipsum</b> dolor sit amet, consectetuer adipiscing elit. Maecenas porttitor congue massa. Fusce posuere, magna sed pulvinar ultricies, purus lectus malesuada libero, sit amet commodo magna eros quis urna.</p>
    <h4>Address</h4><p>1234 Street Address<br>Harborview, Eastland<br>67890 (E.L)</p>
    <h4>Phone</h4><p>0123-456-789</p>
    <h4>FAX</h4><p>0123-456-789</p>
    <h4>Email</h4><p>info@paleharbor.org</p>
    <h4>Website</h4><p>www.paleharbor.org</p>
  </div>
  <div class="socials"><i></i><i></i><i></i><i></i><span>@YOUR<b>COMPANY</b></span></div>
  <footer class="footer"><span class="brand-name">Pale Harbor Guild</span>
    <div class="pager"><span><svg width="10" height="12" viewBox="0 0 10 12"><polyline points="7,1 2,6 7,11" fill="none" stroke="#fff" stroke-width="2.4"/></svg></span><span><svg width="10" height="12" viewBox="0 0 10 12"><polyline points="3,1 8,6 3,11" fill="none" stroke="#fff" stroke-width="2.4"/></svg></span></div>
    <span class="page-no">5</span></footer>
</section>

<section class="slide closing col-b row-3">
  <div class="top-tab"></div>
  <div class="red-band"></div>
  <svg class="chevron left" viewBox="0 0 32 69"><polygon points="32,0 32,69 0,34.5" fill="#fff"/><polygon points="32,14 32,55 13,34.5" fill="#ec1f27"/></svg>
  <div class="badge"><div class="thanks">THANK YOU</div></div>
  <svg class="chevron right" viewBox="0 0 32 69"><polygon points="0,0 0,69 32,34.5" fill="#fff"/><polygon points="0,14 0,55 19,34.5" fill="#ec1f27"/></svg>
  <div class="brand-lockup"><span class="brand-mark"></span><div class="brand-name">Pale Harbor Guild</div></div>
  <div class="presenter"><div class="by">Presentation by</div><div class="name">Daniel Hart</div></div>
  <div class="bottom-bar"></div>
</section>

</body>
</html>
```